Education Certificate

We need a modern yet professional Certificate for those who successfully pass / complete our online Training course.

There are various courses but ONE certificate design required.

the certificate needs to look extremely professional and of value.

```html
<!DOCTYPE html>
<html lang="en">
<head>
<meta charset="utf-8">
<title>Certificate of Completion</title>
<link rel="stylesheet" href="https://fonts.googleapis.com/css2?family=Allura&family=Montserrat:wght@800;900&family=Poppins:wght@400;500;600&display=swap">
<style>
  :root {
    --page-bg: #d9dae3;
    --navy: #213270;
    --navy-deep: #1a1f7a;
    --royal: #2a2fb0;
    --gold: #f2c928;
    --paper: #f1f1f3;
    --ink: #1d1d1f;
    --rule-blue: #2b3a8f;
    --seal-light: #f7dd8a;
    --seal-mid: #d9a53a;
    --seal-dark: #9c6a18;
  }
  * { margin: 0; padding: 0; box-sizing: border-box; }
  html, body { width: 834px; height: 1200px; overflow: hidden; }
  body { background: var(--page-bg); position: relative; font-family: "Poppins", sans-serif; color: var(--ink); }

  .certificate {
    position: absolute; left: 37px; top: 306px; width: 760px; height: 588px;
    box-shadow: 0 6px 18px rgba(20, 24, 60, 0.18);
  }
  .certificate-frame { position: absolute; inset: 0; }

  .brand-block {
    position: absolute; left: 309px; top: 42px; width: 143px; height: 53px;
    background: var(--navy); border: 1px solid #fff;
    display: flex; align-items: center; gap: 8px; padding: 0 8px;
  }
  .brand-square { width: 30px; height: 30px; background: #fff; flex: none; }
  .brand-name {
    color: #fff; font-family: "Poppins", sans-serif; font-weight: 400;
    font-size: 9.5px; line-height: 1.2; text-transform: uppercase;
  }

  .title {
    position: absolute; left: 0; right: 0; top: 103px; text-align: center;
    font-family: "Montserrat", sans-serif; font-weight: 900; font-size: 55px;
    line-height: 1; letter-spacing: -0.5px; color: var(--ink);
  }
  .ribbon { position: absolute; left: 145px; top: 170px; width: 470px; height: 62px; }
  .ribbon-text {
    position: absolute; left: 205px; top: 170px; width: 350px; height: 44px;
    display: flex; align-items: center; justify-content: center;
    font-family: "Montserrat", sans-serif; font-weight: 800; font-size: 27px;
    letter-spacing: 5px; color: #fff;
  }
  .presented {
    position: absolute; left: 0; right: 0; top: 232px; text-align: center;
    font-size: 15px; font-weight: 500; letter-spacing: 8px; padding-left: 8px;
  }
  .recipient {
    position: absolute; left: 0; right: 0; top: 258px; text-align: center;
    font-family: "Allura", cursive; font-size: 70px; line-height: 1;
  }
  .recipient-rule { position: absolute; left: 83px; width: 593px; top: 334px; height: 1px; background: var(--ink); }
  .statement {
    position: absolute; left: 0; right: 0; top: 346px; text-align: center;
    font-size: 18px; font-weight: 500;
  }
  .field-label { position: absolute; font-size: 17px; font-weight: 500; }
  .field-rule { position: absolute; height: 1px; background: var(--rule-blue); }
  .sign-label { position: absolute; font-size: 17px; font-weight: 400; text-align: center; width: 186px; }

  .seal { position: absolute; left: 333px; top: 432px; width: 94px; height: 94px; }
</style>
</head>
<body>
  <main class="certificate">
    <svg class="certificate-frame" width="760" height="588" viewBox="0 0 760 588" aria-hidden="true">
      <rect width="760" height="588" fill="var(--navy)"/>
      <path d="M49,27 H711 A22 22 0 0 0 733,49 V539 A22 22 0 0 0 711,561 H49 A22 22 0 0 0 27,539 V49 A22 22 0 0 0 49,27 Z"
            fill="var(--paper)" stroke="var(--gold)" stroke-width="3"/>
      <path d="M53,33 H707 A20 20 0 0 0 727,53 V535 A20 20 0 0 0 707,555 H53 A20 20 0 0 0 33,535 V53 A20 20 0 0 0 53,33 Z"
            fill="none" stroke="var(--navy)" stroke-width="1.5"/>
    </svg>

    <div class="brand-block">
      <span class="brand-square"></span>
      <span class="brand-name">Northbridge<br>Service<br>Academy</span>
    </div>

    <h1 class="title">CERTIFICATE</h1>

    <svg class="ribbon" viewBox="0 0 470 62" aria-hidden="true">
      <defs>
        <linearGradient id="band" x1="0" x2="1" y1="0" y2="0">
          <stop offset="0" stop-color="var(--navy-deep)"/>
          <stop offset="0.5" stop-color="var(--royal)"/>
          <stop offset="1" stop-color="var(--navy-deep)"/>
        </linearGradient>
        <linearGradient id="tailL" x1="0" x2="1">
          <stop offset="0" stop-color="#1c2fa6"/><stop offset="1" stop-color="#1a1f6b"/>
        </linearGradient>
        <linearGradient id="tailR" x1="1" x2="0">
          <stop offset="0" stop-color="#1c2fa6"/><stop offset="1" stop-color="#1a1f6b"/>
        </linearGradient>
      </defs>
      <polygon points="0,24 88,24 88,62 0,62 28,43" fill="url(#tailL)"/>
      <polygon points="470,24 382,24 382,62 470,62 442,43" fill="url(#tailR)"/>
      <polygon points="60,44 88,62 88,44" fill="#0e1350"/>
      <polygon points="410,44 382,62 382,44" fill="#0e1350"/>
      <rect x="60" y="0" width="350" height="44" fill="url(#band)"/>
    </svg>
    <div class="ribbon-text">OF COMPLETION</div>

    <p class="presented">PRESENTED TO</p>
    <p class="recipient">Daniel Carter</p>
    <div class="recipient-rule"></div>

    <p class="statement">For successfully completing our online training course</p>

    <span class="field-label" style="left:83px; top:382px;">From</span>
    <div class="field-rule" style="left:146px; width:238px; top:400px;"></div>
    <span class="field-label" style="left:406px; top:382px;">To</span>
    <div class="field-rule" style="left:439px; width:238px; top:400px;"></div>

    <div class="field-rule" style="left:84px; width:186px; top:477px;"></div>
    <span class="sign-label" style="left:84px; top:480px;">Signature</span>
    <div class="field-rule" style="left:490px; width:186px; top:477px;"></div>
    <span class="sign-label" style="left:490px; top:482px;">Date</span>

    <svg class="seal" viewBox="0 0 94 94" role="img" aria-label="Gold seal of authenticity">
      <defs>
        <radialGradient id="sealFill" cx="0.4" cy="0.35" r="0.7">
          <stop offset="0" stop-color="var(--seal-light)"/>
          <stop offset="0.6" stop-color="var(--seal-mid)"/>
          <stop offset="1" stop-color="var(--seal-dark)"/>
        </radialGradient>
      </defs>
      <circle cx="47" cy="47" r="46" fill="url(#sealFill)"/>
      <circle cx="47" cy="47" r="33" fill="#f6efdc" stroke="var(--seal-mid)" stroke-width="3"/>
    </svg>
  </main>
</body>
</html>
```